Folded A4 flyer for design&construction company

Folded A4 flyer needed. Keywords: elegant, stylish
our website www.corvimo.ae

Industry/Entity Type

Construction

```html
<!DOCTYPE html>
<html lang="en">
<head>
<meta charset="utf-8">
<title>Corvimo – Folded Flyer</title>
<link rel="stylesheet" href="https://fonts.googleapis.com/css2?family=Lato:wght@400;700;900&display=swap">
<style>
  :root {
    --bg: #d9d9da;
    --paper: #ffffff;
    --ink: #262422;
    --charcoal: #2f2d2b;
    --charcoal-deep: #1f1e1d;
    --gold: #d1ad3a;
    --gold-light: #ecd46a;
    --gold-dark: #a88424;
    --text-muted: #555;
  }
  * { box-sizing: border-box; margin: 0; padding: 0; }
  html, body { width: 1200px; height: 806px; overflow: hidden; }
  body {
    background: var(--bg);
    font-family: "Lato", Arial, sans-serif;
    position: relative;
  }
  .panel {
    position: absolute;
    top: 33px;
    width: 523px;
    height: 740px;
    background: var(--paper);
    overflow: hidden;
  }
  .panel--back { left: 77px; }
  .panel--front { left: 600px; }

  .gold-band {
    position: absolute; left: 0; right: 0;
    background: linear-gradient(90deg, var(--gold-dark), var(--gold-light) 45%, var(--gold) 70%, var(--gold-dark));
  }
  .gold-rule {
    position: absolute; left: 0; right: 0; height: 4px;
    background: linear-gradient(90deg, var(--gold-dark), var(--gold-light), var(--gold-dark));
  }
  .dark-field {
    position: absolute; left: 0; right: 0;
    background: radial-gradient(ellipse at 50% 40%, #3d3a37 0%, var(--charcoal) 55%, var(--charcoal-deep) 100%);
  }

  .brand {
    position: absolute; left: 0; right: 0;
    display: flex; align-items: center; justify-content: center; gap: 12px;
    font-weight: 400; letter-spacing: 2px;
  }
  .brand__dot { width: 14px; height: 14px; border-radius: 50%; background: var(--gold); }
  .brand--light { color: #fff; font-size: 46px; top: 175px; }
  .brand--dark { color: var(--ink); font-size: 38px; top: 40px; }

  .quote {
    position: absolute; left: 0; right: 0; top: 330px;
    text-align: center; color: #fff; font-size: 16px; letter-spacing: .4px;
  }

  .photo {
    position: absolute;
    border: 4px solid var(--gold);
    box-shadow: 0 3px 8px rgba(0,0,0,.35);
  }
  .photo--white-room { left: 92px; top: 468px; width: 168px; height: 120px;
    background: linear-gradient(135deg, #f3f1ed, #cfcac2 60%, #e8e4dc); }
  .photo--lounge { left: 270px; top: 458px; width: 168px; height: 120px;
    background: linear-gradient(135deg, #e8d6b4, #b98a55 55%, #d9c29a); }
  .photo--hall { left: 18px; top: 130px; width: 487px; height: 250px; border: none; box-shadow: none;
    background: linear-gradient(100deg, #e9e2d6 0%, #6b5a4b 30%, #8a6038 55%, #b9763a 75%, #efe6d9 100%); }

  .web {
    position: absolute; left: 0; right: 0; text-align: center;
    font-weight: 700; letter-spacing: 5px; color: var(--ink); font-size: 20px;
  }
  .address {
    position: absolute; left: 0; right: 0; text-align: center;
    color: var(--text-muted); font-size: 12px; font-weight: 700;
  }

  .about-band { top: 388px; height: 110px; }
  .about {
    position: absolute; left: 28px; right: 28px; top: 401px;
    text-align: center; font-size: 11px; font-weight: 700; line-height: 1.32; color: var(--ink);
  }
  .cta {
    position: absolute; left: 0; right: 0; top: 545px;
    display: flex; justify-content: center; align-items: center; gap: 16px;
  }
  .cta__offer { color: var(--gold-light); font-weight: 900; font-size: 22px; line-height: 1.15; text-align: right; }
  .cta__divider { width: 2px; height: 64px; background: var(--gold); }
  .cta__contact { color: #fff; font-size: 22px; line-height: 1.2; }
  .cta__contact small { font-size: 18px; }

  .web-pill {
    position: absolute; top: 642px; left: 50%; transform: translateX(-50%);
    width: 240px; height: 26px; border-radius: 13px;
    background: linear-gradient(90deg, var(--gold-dark), var(--gold-light), var(--gold-dark));
    text-align: center; line-height: 26px; font-weight: 700; letter-spacing: 4px; font-size: 14px; color: var(--ink);
  }
  .web-pill::before, .web-pill::after {
    content: ""; position: absolute; top: 12px; width: 45px; height: 1px; background: var(--gold);
  }
  .web-pill::before { left: -55px; }
  .web-pill::after { right: -55px; }
</style>
</head>
<body>

<section class="panel panel--back">
  <div class="gold-band" style="top:28px;height:24px"></div>
  <div class="dark-field" style="top:52px;height:468px"></div>
  <div class="gold-rule" style="top:520px"></div>

  <div class="brand brand--light"><span class="brand__dot"></span>CORVIMO</div>
  <p class="quote">Quality is not an act, it is a habit – Elias Varn</p>

  <div class="photo photo--white-room" role="img" aria-label="Bright white living room interior"></div>
  <div class="photo photo--lounge" role="img" aria-label="Warm classic lounge with armchairs"></div>

  <p class="web" style="top:630px">www.corvimo.ae</p>
  <p class="address" style="top:664px">Corvimo LLC, Marina Crest Tower, Office 902, Business Bay, Dubai</p>
</section>

<section class="panel panel--front">
  <div class="brand brand--dark"><span class="brand__dot"></span>CORVIMO</div>
  <div class="gold-rule" style="top:116px"></div>

  <div class="photo photo--hall" role="img" aria-label="Classic living hall with stone fireplace and wooden floor"></div>

  <div class="gold-band about-band"></div>
  <p class="about">We believe in quality beginnings and flawless finishes. We are a team of creative designers and constructors with years of experience and expertise in providing complete interior design and construction services. Our unique designing prowess is complemented by our unflinching commitment to quality construction. Our team specializes in classic and contemporary high quality construction in Dubai for commercial and residential projects.</p>

  <div class="dark-field" style="top:506px;height:234px"></div>
  <div class="cta">
    <p class="cta__offer">GET A FREE<br>QUOTE TODAY!</p>
    <span class="cta__divider"></span>
    <p class="cta__contact">800 – CORVIMO OR<br><small>CONTACT@CORVIMO.AE</small></p>
  </div>

  <p class="web-pill">www.corvimo.ae</p>
  <p class="address" style="top:684px;color:#ccc;font-weight:400">Corvimo LLC, Marina Crest Tower, Office 902, Business Bay, Dubai</p>
</section>

</body>
</html>
```